Indie Poet needs book cover!

I am looking for a design that will sell my poetry book. My poems deal with themes of neurotic and dark Gothic narrative. A combination of these two styles is ideal.

The dimensions for the book cover are:

Place 5mm bleed around entire cover.

Width: 148mm (back) + 4.45mm (spine) + 148mm (front)

Height: 220mm

Front Cover:

Book Title: Lanterns Under Glass: The Verses of Maud Delacorte

Author: Maud Delacorte

Please place the 'Curator's Pick' logo on the front cover. Beneath it, please put : quillmarkAUSTRALIA 2014 - For the poem 'Waiting by the Well'.

Spine: Lanterns Under Glass: The Verses of Maud Delacorte

Back Cover:

Include 'The Widow' picture on the back cover.

Text:

About the book:
'Lanterns Under Glass' is an impressive work for a debut release, featuring poems that have a maturity and level of experience you’d expect from poets who have been in the industry for decades. The poems and stories are complex, yet easy to associate with, and there would be few readers who wouldn't find themselves resonating with the themes. For all the cynicism and neuroticism, there is an underlying story about life and people.

Note: please leave SPACE for barcode. Do not add a barcode, just leave room for one.

```html
<!DOCTYPE html>
<html lang="en">
<head>
<meta charset="utf-8">
<title>Lanterns Under Glass – Book Cover</title>
<link rel="stylesheet" href="https://fonts.googleapis.com/css2?family=Marcellus&family=Marcellus+SC&family=Tinos:ital,wght@1,400;1,700&display=swap">
<style>
  :root {
    --paper: #ffffff;
    --ink: #000000;
    --text-light: #ffffff;
    --gold: #e9d9a0;
    --author-blue: #c9d6ee;
    --spine-rule: #a33a34;
    --flame-core: #cfe0ff;
    --flame-mid: #3a6ee8;
    --flame-deep: #0b1c5a;
    --badge-gold: #d9b64a;
    --badge-light: #f4e3a0;
  }
  * { margin: 0; padding: 0; box-sizing: border-box; }
  html, body { width: 1200px; height: 900px; overflow: hidden; background: var(--paper); }

  .cover-sheet {
    position: relative;
    width: 1200px;
    height: 900px;
    background: var(--paper);
  }
  .cover-wrap {
    position: absolute;
    left: 18px; top: 18px;
    width: 1164px; height: 870px;
    background: var(--ink);
  }

  /* Back cover */
  .back-cover {
    position: absolute;
    left: 0; top: 0;
    width: 567px; height: 870px;
  }
  .blurb {
    position: absolute;
    left: 95px; top: 82px;
    width: 360px;
    color: var(--text-light);
    font-family: "Tinos", "Times New Roman", serif;
    font-style: italic;
    font-size: 24px;
    line-height: 32.2px;
    text-align: center;
  }
  .blurb .book-name { display: block; font-size: 25px; line-height: 28px; }
  .barcode-space {
    position: absolute;
    left: 301px; top: 774px;
    width: 242px; height: 60px;
    background: var(--paper);
    display: flex; align-items: center; justify-content: center;
    font-family: "Tinos", "Times New Roman", serif;
    font-style: italic; font-weight: 700;
    font-size: 18px;
    color: var(--ink);
  }

  /* Spine */
  .spine {
    position: absolute;
    left: 567px; top: 0;
    width: 28px; height: 870px;
    border-left: 1.5px solid var(--spine-rule);
    border-right: 1.5px solid var(--spine-rule);
  }
  .spine-title {
    position: absolute;
    left: 1px; top: 38px;
    writing-mode: vertical-rl;
    white-space: nowrap;
    font-family: "Marcellus", "Times New Roman", serif;
    font-size: 19px;
    letter-spacing: 2.4px;
    color: var(--text-light);
  }
  .spine-title .spine-sub {
    font-family: "Tinos", "Times New Roman", serif;
    font-style: italic; font-weight: 700;
    letter-spacing: 0.6px;
    color: var(--gold);
  }

  /* Front cover */
  .front-cover {
    position: absolute;
    left: 595px; top: 0;
    width: 569px; height: 870px;
  }
  .book-title {
    position: absolute;
    left: 0; top: 42px; width: 569px;
    text-align: center;
    font-family: "Marcellus", "Times New Roman", serif;
    font-weight: 400;
    font-size: 58px;
    line-height: 62px;
    letter-spacing: 3px;
    color: var(--text-light);
  }
  .book-subtitle {
    position: absolute;
    left: 0; top: 190px; width: 569px;
    text-align: center;
    font-family: "Tinos", "Times New Roman", serif;
    font-style: italic;
    font-size: 25px;
    letter-spacing: 4.2px;
    color: var(--gold);
  }
  .cover-artwork {
    position: absolute;
    left: 80px; top: 225px;
    width: 380px; height: 480px;
  }
  .award-seal {
    position: absolute;
    left: 368px; top: 588px;
    width: 96px; height: 96px;
  }
  .award-caption {
    position: absolute;
    left: 215px; top: 690px; width: 360px;
    text-align: center;
    font-family: "Marcellus SC", "Times New Roman", serif;
    font-size: 12px;
    line-height: 23px;
    letter-spacing: 2.6px;
    color: var(--text-light);
  }
  .author-name {
    position: absolute;
    left: 0; top: 784px; width: 630px;
    text-align: center;
    font-family: "Marcellus SC", "Times New Roman", serif;
    font-size: 36px;
    letter-spacing: 5px;
    color: var(--author-blue);
  }
</style>
</head>
<body>
<main class="cover-sheet">
  <div class="cover-wrap">

    <section class="back-cover">
      <p class="blurb">
        <span class="book-name">‘Lanterns Under Glass’</span>
        is an impressive work for a<br>
        debut release, featuring poems<br>
        that have a maturity and level<br>
        of experience you’d expect<br>
        from poets who have been<br>
        in the industry for decades.<br>
        The poems and stories are<br>
        complex, yet easy to<br>
        associate with, and<br>
        there would be<br>
        few readers who wouldn't<br>
        find themselves<br>
        resonating with the themes.<br>
        For all the cynicism and<br>
        neuroticism, there is an<br>
        underlying<br>
        story about life<br>
        and people.
      </p>
      <div class="barcode-space">BAR CODE</div>
    </section>

    <section class="spine">
      <h2 class="spine-title">LANTERNS UNDER GLASS: <span class="spine-sub">The Verses of Maud Delacorte</span></h2>
    </section>

    <section class="front-cover">
      <h1 class="book-title">LANTERNS UNDER<br>GLASS</h1>
      <p class="book-subtitle">The Verses of Maud Delacorte</p>

      <svg class="cover-artwork" viewBox="0 0 380 480" role="img" aria-label="Glowing blue brain engulfed in blue flames">
        <defs>
          <radialGradient id="flameGlow" cx="50%" cy="42%" r="55%">
            <stop offset="0%" stop-color="var(--flame-core)"/>
            <stop offset="35%" stop-color="var(--flame-mid)"/>
            <stop offset="75%" stop-color="var(--flame-deep)"/>
            <stop offset="100%" stop-color="var(--ink)" stop-opacity="0"/>
          </radialGradient>
        </defs>
        <ellipse cx="190" cy="220" rx="190" ry="240" fill="url(#flameGlow)"/>
      </svg>

      <svg class="award-seal" viewBox="0 0 96 96" aria-hidden="true">
        <defs>
          <radialGradient id="sealGold" cx="40%" cy="35%" r="70%">
            <stop offset="0%" stop-color="var(--badge-light)"/>
            <stop offset="100%" stop-color="var(--badge-gold)"/>
          </radialGradient>
        </defs>
        <circle cx="48" cy="48" r="47" fill="url(#sealGold)"/>
      </svg>

      <p class="award-caption">quillmark AUSTRALIA 2014 -<br>For the poem 'Waiting by the Well'</p>

      <p class="author-name">Maud Delacorte</p>
    </section>

  </div>
</main>
</body>
</html>
```